Flyer for Compassion training days

I need a A5-size, single-sided flyer design for my training days. They are weekends in a blend of Orbisan Communication and Buddhist teachings called Verbane Communication. The logo for Verbane that should be included.
The flyer needs room for 1) course title, 2) course dates, location & price, 3) course description, 4) booking info, 5) my picture & short bio, and 6) the verbane.co website (yes, it is 'co' and not 'com).

Target Market(s)

Women 35-65 years, well-educated, spiritually minded. May have interests like yoga and meditation.

Industry/Entity Type

Health And Wellness

Font styles to use
Sans Serif
Other font styles liked:
• Blue Plaque, Josefina are both great

Colors
fbf289
fdf9cf
cfeae6
33b8a4

Requirements
Must have
• The Verbane logo; my picture.
• Elegance. Calm and expansive feel.
• The poster provided in the project files shows you the kind of information I need to include.
• Colours -- greens and yellows, but the options on sketch harbor are not quite the right shades.
• The logo colour can be changed.
Nice to have
• Classy (but not cliche) image associated with Buddhism; gentle curves similar to those on the business card (see project files).
Should not have
• Dark background. Busy, loud design. Overly 'swirly' design. Images that I have to buy separately.

```html
<!DOCTYPE html>
<html lang="en">
<head>
<meta charset="utf-8">
<title>Verbane Communication – Core Course Flyer</title>
<link rel="stylesheet" href="https://fonts.googleapis.com/css2?family=Josefin+Sans:wght@400;600;700&display=swap">
<style>
  :root {
    --backdrop: #eef2ea;
    --paper: #fdfae4;
    --paper-light: #fffef5;
    --paper-edge: #f4f0c8;
    --green: #2aae4a;
    --green-light: #7fcf63;
    --mint: #cfeae6;
    --ink: #2a2a28;
    --ink-soft: #3d3d3a;
    --bronze-light: #c9b79a;
    --bronze-dark: #6f5c45;
    --sepia-light: #c8a46a;
    --sepia-dark: #6e4c23;
  }
  * { box-sizing: border-box; margin: 0; padding: 0; }
  html, body {
    width: 1200px; height: 1200px; overflow: hidden;
    background: var(--backdrop);
    font-family: "Josefin Sans", "Century Gothic", sans-serif;
    color: var(--ink);
  }
  .flyer {
    position: absolute; left: 214px; top: 52px;
    width: 771px; height: 1096px;
    background: radial-gradient(ellipse at 55% 45%, var(--paper-light) 0%, var(--paper) 55%, var(--paper-edge) 100%);
    overflow: hidden;
  }
  .bubbles {
    position: absolute; inset: 0;
    background:
      radial-gradient(circle at 88% 40%, rgba(207,234,230,.55) 0 60px, transparent 61px),
      radial-gradient(circle at 78% 54%, rgba(207,234,230,.45) 0 40px, transparent 41px),
      radial-gradient(circle at 70% 88%, rgba(207,234,230,.5) 0 55px, transparent 56px),
      radial-gradient(circle at 92% 95%, rgba(207,234,230,.45) 0 45px, transparent 46px),
      radial-gradient(circle at 20% 72%, rgba(207,234,230,.35) 0 35px, transparent 36px);
  }
  .statue {
    position: absolute; left: 48px; top: 54px; width: 220px; height: 368px;
    border-radius: 45% 40% 20% 30% / 30% 30% 20% 25%;
    background: linear-gradient(160deg, var(--bronze-light), var(--bronze-dark));
  }
  .swirls {
    position: absolute; left: 480px; top: 190px; width: 291px; height: 420px;
    background: radial-gradient(ellipse at 60% 40%, rgba(251,242,137,.35), rgba(207,234,230,.15) 60%, transparent 75%);
  }
  .brand {
    position: absolute; left: 500px; top: 70px;
    display: flex; align-items: center; gap: 12px;
  }
  .brand-dot { width: 40px; height: 40px; border-radius: 50%; background: var(--green); }
  .brand-name { font-size: 32px; font-weight: 600; color: var(--green); }
  .headline {
    position: absolute; left: 280px; width: 430px; top: 220px;
    text-align: center; font-weight: 600; color: var(--ink);
  }
  .headline-formula { font-size: 24px; line-height: 38px; }
  .headline-title { font-size: 35px; line-height: 50px; font-weight: 700; }
  .ribbon {
    position: absolute; left: 262px; top: 416px; width: 261px; height: 38px;
    background: var(--green); color: #fff;
    font-size: 27px; text-align: center; line-height: 42px;
    clip-path: polygon(0 0, 100% 0, 96% 50%, 100% 100%, 0 100%, 4% 50%);
  }
  .details {
    position: absolute; left: 160px; width: 480px; top: 460px;
    text-align: center; font-size: 25px; line-height: 34px; font-weight: 600;
  }
  .description {
    position: absolute; left: 45px; top: 550px; width: 680px;
    font-size: 15.5px; line-height: 21.5px; color: var(--ink-soft);
  }
  .description p { margin-bottom: 6px; }
  .topics { list-style: none; margin: 4px 0 10px; }
  .topics li { display: flex; align-items: center; gap: 10px; padding-left: 14px; line-height: 24px; }
  .topics svg { flex: none; }
  .booking {
    position: absolute; left: 0; top: 840px; height: 35px;
    display: flex; align-items: center;
  }
  .booking-tag {
    width: 161px; height: 35px; background: var(--green-light); color: #fff;
    font-size: 23px; line-height: 39px; padding-left: 30px;
    clip-path: polygon(0 0, 92% 0, 100% 50%, 92% 100%, 0 100%);
  }
  .booking-text { margin-left: 10px; font-size: 21px; font-weight: 600; }
  .portrait {
    position: absolute; left: 48px; top: 907px; width: 142px; height: 139px;
    border-radius: 10px; border: 2px solid #8c8c8c;
    background: linear-gradient(150deg, var(--sepia-light), var(--sepia-dark));
  }
  .bio {
    position: absolute; left: 199px; top: 922px; width: 500px;
    font-size: 15.5px; line-height: 20px; font-weight: 600; color: var(--ink-soft);
  }
  .bio p { margin-bottom: 6px; }
</style>
</head>
<body>
  <main class="flyer">
    <div class="bubbles"></div>
    <div class="swirls" role="img" aria-label="Soft floral swirls with a butterfly"></div>
    <div class="statue" role="img" aria-label="Bronze statue of a resting seated Buddha"></div>

    <div class="brand">
      <span class="brand-dot"></span>
      <span class="brand-name">Verbane.co</span>
    </div>

    <header class="headline">
      <div class="headline-formula">Mindfulness + Kindness +</div>
      <div class="headline-formula">Orbisan Communication =</div>
      <h1 class="headline-title">Verbane Communication</h1>
    </header>

    <div class="ribbon">CORE COURSE</div>

    <div class="details">
      <div>11-12 Dec; Thornbury Hall, Edinburgh</div>
      <div>(£125/100)</div>
    </div>

    <section class="description">
      <p>Verbane Communication can help you increase awareness &amp; compassion in everyday speech (with yourself &amp; others), better understand your own patterns, and build resilience to challenging situations. Choose from:</p>
      <p>In this 2-day Core Course, we’ll explore:</p>
      <ul class="topics">
        <li><svg width="16" height="14" viewBox="0 0 16 14"><path d="M2 12 C2 4 8 1 14 2 C13 9 8 12 2 12 Z" fill="#2aae4a"/></svg>Orbisan Communication;</li>
        <li><svg width="16" height="14" viewBox="0 0 16 14"><path d="M2 12 C2 4 8 1 14 2 C13 9 8 12 2 12 Z" fill="#2aae4a"/></svg>Buddhist teachings on Right Speech, loving-kindness, Right Effort, and more;</li>
        <li><svg width="16" height="14" viewBox="0 0 16 14"><path d="M2 12 C2 4 8 1 14 2 C13 9 8 12 2 12 Z" fill="#2aae4a"/></svg>mindfulness practices;</li>
        <li><svg width="16" height="14" viewBox="0 0 16 14"><path d="M2 12 C2 4 8 1 14 2 C13 9 8 12 2 12 Z" fill="#2aae4a"/></svg>choices available to us in our everyday speech.</li>
      </ul>
      <p>This workshop will be of interest if you’d like to improve personal and/or professional relationships.&nbsp; Open to all, best suited to those with at least 1 year’s experience with Mindfulness,&nbsp; Buddhism, or Orbisan Communication / NVC.</p>
    </section>

    <div class="booking">
      <div class="booking-tag">BOOKING</div>
      <div class="booking-text">Book online at Ticketfold or write maribeth@verbane.co</div>
    </div>

    <div class="portrait" role="img" aria-label="Portrait photo of the facilitator"></div>
    <section class="bio">
      <p>Facilitator: Maribeth Quillon is an experienced group facilitator, having worked with a range of organisations and presented at a number of festivals &amp; conferences.</p>
      <p>Maribeth offers coaching in Verbane Communication.</p>
      <p>For more info, please visit website www.verbane.co</p>
    </section>
  </main>
</body>
</html>
```